Tomas Whitlow Design, LLC (www.tomaswhitlow.design)

A very hip, trendy architectural home page. Simple Menu upper right hand corner (About, Projects, Inspiration, Design-Build, Contact). In the "Projects" ... I want to click on each project and that will open up multiple photo's of that project. Attached are the graphics of my logo. I want the home page to be incredible ... I really market my name "Tomas Whitlow" as sophisticated architecture. Colors/branding should be black/metallic/white/grey maybe with a pop of a bright color but not much. My architecture is like www.brennerfaulkatelier.com if you want to review as example. My specialty is industrial design, homes with architectural concrete design, steel beams, alot of glass. Very modern. My work is best illustrated at www.vasquerlind.com.
Updates

Please see images uploaded in my brief. A new business card design by an AWESOME designer and some inspirational architectural projects I worked on.

Industry/Entity Type

Architecture

Coding

Coded - Design and coding required

Number of Pages Required

5+ page

Colors

Designer to choose only greyscale colors for use in the design.

Requirements
Must have
• The 1st project photo gallery is called "Raw Dwelling at Cypress Point"... Images of this project can be taken from: https://www.homeplotra.com/homedetails/2817-9th-St-SE-Naples-FL-34117/508164229_zpid/

The 2nd project photo gallery is called "Stone, Iron and Timber Residence at Cypress Point". I will upload images for this project but use placeholder until I finalize.

The 3rd photo gallery is called "Early Sketches: Off the Page". I will forward pictures. for this.

Website should be easy to update and handover at completion as we will be updating frequently. Wordpress, WIX, or other type is fine as long as it looks profesional and high-class.
Nice to have
• Maybe the home page loads to just "Tomas Whitlow Design, LLC ... Atelier for Bold Structural Vision" and has a click to enter button. Something cool maybe a fade it or something eye-catching and cool.
Should not have
• Should not be overly colorful.

```html
<!DOCTYPE html>
<html lang="en">
<head>
<meta charset="utf-8">
<title>Tomas Whitlow Design, LLC</title>
<link href="https://fonts.googleapis.com/css2?family=Fira+Sans:wght@300;400;500;600;700;800&family=Fira+Sans+Condensed:wght@500&display=swap" rel="stylesheet">
<style>
:root{
  --ink:#111214;
  --charcoal:#1d1e20;
  --night:#0f1a2e;
  --white:#ffffff;
  --grey:#9a9ca0;
  --grey-light:#b8babd;
  --line:#e4e5e7;
  --strip:#eef0f2;
  --footer:#1e1e1f;
  --footer-bar:#171718;
}
*{margin:0;padding:0;box-sizing:border-box}
html,body{width:1200px;height:2680px;overflow:hidden;background:var(--white)}
body{position:relative;font-family:"Fira Sans",sans-serif;color:var(--ink)}
.abs{position:absolute}

/* splash */
.splash{left:0;top:0;width:1200px;height:675px;background:linear-gradient(180deg,#1c2c48 0%,#33476a 30%,#2a2a26 55%,#6b5236 75%,#3a2a22 100%)}
.splash-brand{left:0;top:70px;width:1200px;text-align:center;color:var(--white)}
.splash-mark{display:inline-block;width:74px;height:74px;border:3px solid var(--white)}
.splash-rule{width:172px;height:2px;background:var(--white);margin:28px auto 22px}
.splash-name{font-size:46px;font-weight:300;letter-spacing:2px}
.splash-sub{font-size:17px;font-weight:400;letter-spacing:9px;margin-top:8px}
.enter-btn{left:487px;top:400px;width:230px;height:58px;background:var(--white);color:#222;font-size:21px;font-weight:500;letter-spacing:2px;display:flex;align-items:center;justify-content:center;box-shadow:4px 4px 0 -1px rgba(255,255,255,.55)}

/* header + hero */
.hero-photo{left:97px;top:675px;width:1103px;height:646px;background:linear-gradient(180deg,#0e1d3e 0%,#1e2f55 35%,#6e5f3e 62%,#3d3a2c 82%,#2f5a2c 100%)}
.logo-box{left:0;top:675px;width:155px;height:124px;background:var(--white);display:flex;flex-direction:column;align-items:center;justify-content:center;gap:6px}
.logo-box .mark{width:34px;height:34px;border:2px solid var(--ink)}
.logo-box .name{font-size:13px;font-weight:400;color:var(--ink)}
.logo-box .sub{font-size:7px;letter-spacing:3px;color:var(--ink)}
.nav{left:416px;top:699px;display:flex;gap:29px;font-size:9px;font-weight:500;color:var(--white);letter-spacing:.3px}
.nav .active{border-bottom:1px solid var(--white);padding-bottom:6px}
.touch-btn{left:1067px;top:689px;width:87px;height:31px;border:1px solid var(--white);color:var(--white);font-size:8px;font-weight:700;display:flex;align-items:center;justify-content:center}
.social{left:20px;top:938px;width:52px;display:flex;flex-direction:column;gap:36px;font-size:10px;font-weight:600;color:var(--ink);text-align:center}
.hero-title{left:255px;top:815px;color:var(--white);font-size:94px;font-weight:700;line-height:125px;letter-spacing:1px}
.view-btn{left:262px;top:1205px;width:106px;height:36px;border:1.5px solid var(--white);color:var(--white);font-size:7.5px;font-weight:700;display:flex;align-items:center;justify-content:center}
.arrow-btn{top:1328px;width:37px;height:37px;background:var(--charcoal);display:flex;align-items:center;justify-content:center}

/* latest work */
.section-title{left:0;top:1382px;width:1200px;text-align:center;font-size:38px;font-weight:700;letter-spacing:1px}
.section-lede{left:0;top:1448px;width:1200px;text-align:center;font-size:15.5px;font-weight:300;color:var(--grey);line-height:25px;letter-spacing:.6px}
.card{top:1569px;width:369px;height:557px;border:1.5px solid var(--line);background:var(--white)}
.card-photo{position:absolute;left:10px;top:10px;width:347px;height:318px}
.tag{position:absolute;left:0;bottom:0;background:var(--ink);color:var(--white);font-size:12px;font-weight:600;padding:5px 23px}
.card-meta{position:absolute;left:24px;top:358px;font-size:13px;font-weight:300;color:var(--grey-light);letter-spacing:.4px}
.card-meta .dots{margin:0 14px 0 16px;color:#777;letter-spacing:1px}
.card-title{position:absolute;left:24px;top:390px;font-size:19px;font-weight:400;letter-spacing:.8px;color:var(--ink)}
.card-text{position:absolute;left:24px;top:432px;width:325px;font-size:13.5px;font-weight:300;color:var(--grey);line-height:23px;letter-spacing:.4px}
.card-link{position:absolute;left:24px;top:514px;font-size:14px;font-weight:500;display:flex;align-items:center;gap:7px}
.all-btn{left:545px;top:2151px;width:110px;height:36px;background:var(--ink);color:var(--white);font-size:7.5px;font-weight:700;display:flex;align-items:center;justify-content:center;box-shadow:3px 3px 0 0 #fff,4px 4px 0 0 #333}

/* call to action */
.cta{left:0;top:2215px;width:1200px;height:147px;background:linear-gradient(90deg,#0c0c0d,#1b1b1d 60%,#151516)}
.cta-title{left:218px;top:2261px;font-size:28px;font-weight:600;color:var(--white);letter-spacing:.6px}
.cta-text{left:218px;top:2301px;font-size:12px;font-weight:300;color:#9c9c9c;letter-spacing:.3px}
.cta-btn{left:878px;top:2270px;width:109px;height:33px;background:var(--white);color:var(--ink);font-size:7.5px;font-weight:700;display:flex;align-items:center;justify-content:center;box-shadow:3px 3px 0 0 #777}
.strip{left:0;top:2362px;width:1200px;height:26px;background:var(--strip)}

/* footer */
.footer{left:0;top:2388px;width:1200px;height:292px;background:var(--footer);color:#e7e7e7}
.footer-bar{left:0;top:2640px;width:1200px;height:40px;background:var(--footer-bar);border-top:1px solid #2c2c2e}
.f-logo{left:216px;top:2447px;display:flex;align-items:center;gap:10px;color:var(--white)}
.f-logo .mark{width:28px;height:28px;border:2px solid var(--white)}
.f-logo .name{font-size:15px;font-weight:400;border-left:1px solid #888;padding-left:12px}
.f-tagline{left:216px;top:2502px;width:120px;font-size:10px;font-weight:400;line-height:15px;color:#ddd}
.f-social{left:216px;top:2553px;display:flex;gap:18px;font-size:7.5px;font-weight:600;color:#ddd}
.f-head{top:2463px;font-size:11px;font-weight:600;color:var(--white)}
.f-row{display:flex;gap:12px;font-size:9.5px;line-height:16px;color:#cfcfcf;font-weight:400}
.f-list{font-size:9.5px;line-height:16px;color:#cfcfcf}
.f-input{left:822px;top:2497px;width:160px;height:20px;background:#f2f2f2;border:1px solid #555;font-size:9px;color:#aaa;padding:3px 5px}
.f-sub-text{left:822px;top:2533px;width:170px;font-size:9.5px;line-height:16px;color:#cfcfcf}
.copy{left:473px;top:2653px;font-size:9.5px;color:#7e7e7e;letter-spacing:.3px}
.legal{left:833px;top:2653px;display:flex;gap:20px;font-size:9.5px;color:#7e7e7e}
</style>
</head>
<body>

<!-- splash -->
<div class="abs splash" role="img" aria-label="Photograph of a modern concrete and glass house glowing at dusk beneath tall trees"></div>
<div class="abs splash-brand">
  <span class="splash-mark"></span>
  <div class="splash-rule"></div>
  <div class="splash-name">Tomas Whitlow</div>
  <div class="splash-sub">DESIGN LLC</div>
</div>
<div class="abs enter-btn">ENTER WEBSITE</div>

<!-- header and hero -->
<div class="abs hero-photo" role="img" aria-label="Photograph of a concrete-clad modern residence with a glass entrance at night"></div>
<div class="abs logo-box"><span class="mark"></span><span class="name">Tomas Whitlow</span><span class="sub">DESIGN LLC</span></div>
<nav class="abs nav"><span class="active">HOME</span><span>ABOUT</span><span>PROJECTS</span><span>INSPIRATION</span><span>DESIGN-BUILD</span><span>CONTACT</span></nav>
<div class="abs touch-btn">GET IN TOUCH</div>
<div class="abs social"><span>Circle</span><span>Folio</span><span>Network</span><span>Photos</span></div>
<h1 class="abs hero-title">Innovative<br>&amp;<br>Designs</h1>
<div class="abs view-btn">VIEW PROJECTS</div>
<div class="abs arrow-btn" style="left:1081px"><svg width="8" height="10" viewBox="0 0 8 10"><path d="M6 1 2 5l4 4" fill="none" stroke="#fff" stroke-width="1.2"/></svg></div>
<div class="abs arrow-btn" style="left:1124px"><svg width="8" height="10" viewBox="0 0 8 10"><path d="M2 1l4 4-4 4" fill="none" stroke="#fff" stroke-width="1.2"/></svg></div>

<!-- latest work -->
<h2 class="abs section-title">LATEST WORK</h2>
<p class="abs section-lede">Lorem Ipsum Dolor Sit Amet, Consectetuer Adipiscing Elit, Sed Diam<br>Nonummy Tincidunt Ut Laoreet Dolore Magna Aliquam Erat Volutpat.</p>

<article class="abs card" style="left:38px">
  <div class="card-photo" role="img" aria-label="Photograph of a bright kitchen with a timber island and copper pendant lamps" style="background:linear-gradient(180deg,#e9e7e3,#c9c2b6 55%,#8a7460)"><span class="tag">INTERIOR</span></div>
  <div class="card-meta">May 19, 2021<span class="dots">●●</span>Tomas Whitlow</div>
  <h3 class="card-title">Raw Dwelling at Cypress Point</h3>
  <p class="card-text">Occidental in fact, it va esser Occidental. A un Angleso it va semblar un simplificat quam un Europan familie...</p>
  <div class="card-link">Read More <svg width="22" height="10" viewBox="0 0 22 10"><path d="M0 5h20M16 1l4 4-4 4" fill="none" stroke="#111" stroke-width="1.6"/></svg></div>
</article>

<article class="abs card" style="left:415px">
  <div class="card-photo" role="img" aria-label="Photograph of a concrete living room with tall steel-framed windows and leather chairs" style="background:linear-gradient(180deg,#50606a,#8d9296 50%,#b7b2aa)"><span class="tag">INTERIOR</span></div>
  <div class="card-meta">May 19, 2021<span class="dots">●●</span>Tomas Whitlow</div>
  <h3 class="card-title">Raw Dwelling at Cypress Point</h3>
  <p class="card-text">Occidental in fact, it va esser Occidental. A un Angleso it va semblar un simplificat quam un Europan familie...</p>
  <div class="card-link">Read More <svg width="22" height="10" viewBox="0 0 22 10"><path d="M0 5h20M16 1l4 4-4 4" fill="none" stroke="#111" stroke-width="1.6"/></svg></div>
</article>

<article class="abs card" style="left:793px">
  <div class="card-photo" role="img" aria-label="Photograph of an industrial kitchen with a long white counter and dark bar stools under a steel mezzanine" style="background:linear-gradient(180deg,#6f7478,#b9bcbe 45%,#8a8e92 80%,#c8c9ca)"><span class="tag">INTERIOR</span></div>
  <div class="card-meta">May 19, 2021<span class="dots">●●</span>Tomas Whitlow</div>
  <h3 class="card-title">Raw Dwelling at Cypress Point</h3>
  <p class="card-text">Occidental in fact, it va esser Occidental. A un Angleso it va semblar un simplificat quam un Europan familie...</p>
  <div class="card-link">Read More <svg width="22" height="10" viewBox="0 0 22 10"><path d="M0 5h20M16 1l4 4-4 4" fill="none" stroke="#111" stroke-width="1.6"/></svg></div>
</article>

<div class="abs all-btn">VIEW ALL PROJECTS</div>

<!-- call to action -->
<div class="abs cta" role="img" aria-label="Dark background with faint architectural floor plan linework"></div>
<h2 class="abs cta-title">Need More Information? Contact Us</h2>
<p class="abs cta-text">Don't hesitate to reach out, our next big project could be yours</p>
<div class="abs cta-btn">GET IN TOUCH</div>
<div class="abs strip"></div>

<!-- footer -->
<footer class="abs footer"></footer>
<div class="abs f-logo"><span class="mark"></span><span class="name">Tomas Whitlow</span></div>
<p class="abs f-tagline">Atelier for Bold Structural Vision</p>
<div class="abs f-social"><span>Circle</span><span>Folio</span><span>Network</span><span>Photos</span></div>

<div class="abs f-head" style="left:424px">Contact Us</div>
<div class="abs f-row" style="left:424px;top:2503px">
  <svg width="9" height="12" viewBox="0 0 9 12"><path d="M4.5 11.5S1 7 1 4.5a3.5 3.5 0 0 1 7 0C8 7 4.5 11.5 4.5 11.5z" fill="#ddd"/><circle cx="4.5" cy="4.5" r="1.3" fill="#1e1e1f"/></svg>
  <span>5120 Harrowgate Lane<br>Suite 412<br>Naples FL 34110</span>
</div>
<div class="abs f-row" style="left:421px;top:2568px">
  <svg width="14" height="10" viewBox="0 0 14 10"><rect x=".5" y=".5" width="13" height="9" fill="#ddd"/><path d="M.5.5 7 6l6.5-5.5" fill="none" stroke="#1e1e1f"/></svg>
  <span>tomas@tomaswhitlow.design</span>
</div>
<div class="abs f-row" style="left:421px;top:2599px">
  <svg width="12" height="12" viewBox="0 0 12 12"><path d="M2 1l2.2 2.4-1 1.4a7 7 0 0 0 4 4l1.4-1L11 10l-1.4 1.4C5 11 1 7 .6 2.4z" fill="#ddd"/></svg>
  <span>239 555 0184</span>
</div>

<div class="abs f-head" style="left:620px">Latest Projects</div>
<div class="abs f-list" style="left:620px;top:2503px;width:170px">
  <p style="margin-bottom:8px">Raw Dwelling at Cypress Point</p>
  <p style="margin-bottom:8px">Stone, Iron and Timber Residence at Cypress Point</p>
  <p>Early Sketches: Off the Page</p>
</div>

<div class="abs f-head" style="left:822px">Subscribe</div>
<div class="abs f-input">Your Email</div>
<svg class="abs" style="left:962px;top:2502px" width="14" height="11" viewBox="0 0 14 11"><path d="M0 5 14 0 10 11 7 7z" fill="#222"/></svg>
<p class="abs f-sub-text">Subscribe us to follow the latest trends and receive new offers</p>

<div class="abs footer-bar"></div>
<p class="abs copy">Copyright © 2021 Tomas Whitlow. All Rights Reserved.</p>
<div class="abs legal"><span>Terms of use</span><span>Privacy Policy</span></div>

</body>
</html>
```